Flyer für Anbieter für Rennstrecken-trainings
Zielgruppe
wir sind ein professioneller Anbieter für Rennstrecken-trainings ( Motorrad). unsere Zielgruppe sind Motorsport begeisterte jeden alters.
Aufgabenstellung
Ein cleanes modernes design , es gibt exacte vorstellungen

```html
<!DOCTYPE html>
<html lang="de">
<head>
<meta charset="utf-8">
<title>Rennstrecken-Coaching Flyer</title>
<link href="https://fonts.googleapis.com/css2?family=Barlow+Condensed:ital,wght@0,500;0,700;1,500;1,600;1,700;1,800;1,900&display=swap" rel="stylesheet">
<style>
:root{
  --black:#050505;
  --ink:#111111;
  --green:#76a53c;
  --green-bright:#8cc63f;
  --white:#ffffff;
  --divider:#8cb455;
}
*{margin:0;padding:0;box-sizing:border-box}
html,body{width:909px;height:1200px;overflow:hidden;background:var(--white)}
body{font-family:"Barlow Condensed",Arial,sans-serif}
.flyer{position:relative;width:909px;height:1200px;overflow:hidden;background:var(--black)}

/* header */
.header{position:absolute;left:0;top:0;width:909px;height:300px;background:var(--black)}
.title-rule{position:absolute;left:215px;width:480px;height:3px;background:linear-gradient(90deg,transparent,var(--white) 15%,var(--white) 85%,transparent)}
.title{position:absolute;left:0;width:909px;top:54px;text-align:center;color:var(--white);font-style:italic;font-weight:800;font-size:58px;letter-spacing:.5px;line-height:1}
.price-line{position:absolute;left:0;width:909px;top:160px;text-align:center;color:var(--white);font-style:italic;font-weight:800;font-size:62px;line-height:1}
.price-line .amount{color:var(--green);font-size:104px;font-weight:900;vertical-align:-8px}

/* middle area */
.middle{position:absolute;left:0;top:300px;width:909px;height:665px;background:linear-gradient(180deg,#2a2a2a 0%,#cfcfcf 18%,#f0f0f0 50%,#e6e6e6 85%,#6a6a6a 100%)}
.track-photo{position:absolute;right:0;top:300px;width:360px;height:665px;background:linear-gradient(160deg,#d9d9d9 0%,#b4b4b4 55%,#9a6a5a 80%,#cfcfcf 100%);opacity:.75}
.rider-photo{position:absolute;left:676px;top:300px;width:222px;height:140px;border-radius:40% 50% 30% 40%;background:radial-gradient(ellipse at 50% 50%,var(--green-bright) 0%,#2a2a2a 65%,transparent 70%)}

.tab{position:absolute;left:0;background:var(--black);color:var(--white);font-style:italic;font-weight:800;font-size:36px;line-height:1;padding-left:32px;display:flex;align-items:center}

/* included items */
.included{position:absolute;left:0;top:386px;width:817px;height:173px;background:var(--white);border-bottom:4px solid var(--green)}
.included .item{position:absolute;top:0;height:169px}
.included .item + .item{border-left:2px solid var(--divider)}
.included .photo{position:absolute;left:50%;transform:translateX(-50%);top:22px;height:92px;border-radius:10px}
.included .label{position:absolute;left:0;right:0;top:128px;text-align:center;font-style:italic;font-weight:500;font-size:22px;color:var(--ink)}

/* programme */
.programme{position:absolute;left:0;top:628px;width:830px;height:86px;background:linear-gradient(90deg,#3a3a3a 0%,#555 55%,rgba(120,120,120,0) 100%)}
.programme li{list-style:none;display:flex;align-items:center;gap:14px;color:var(--white);font-style:italic;font-weight:500;font-size:31px;line-height:40px;padding-left:40px}
.programme ul{padding-top:3px}

/* equipment */
.equipment{position:absolute;left:0;top:794px;width:676px;height:166px;background:var(--white)}
.equipment .item{position:absolute;top:0;height:166px}
.equipment .item + .item{border-left:2px solid var(--divider)}
.equipment .photo{position:absolute;left:50%;transform:translateX(-50%);top:22px;width:92px;height:88px;border-radius:12px}
.equipment .label{position:absolute;left:0;right:0;top:118px;text-align:center;font-style:italic;font-weight:500;font-size:33px;color:var(--ink)}
.equipment .label.small{font-size:25px;top:124px}
.badge{position:absolute;left:14px;top:18px;width:62px;height:62px;border-radius:50%;background:var(--green);color:var(--white);font-weight:700;font-style:italic;font-size:25px;display:flex;align-items:center;justify-content:center}
.bundle{position:absolute;left:683px;top:790px;width:221px;height:170px;background:var(--green)}
.bundle .amount{position:absolute;left:24px;top:28px;color:var(--white);font-style:italic;font-weight:800;font-size:40px}
.bundle .photo{position:absolute;left:110px;top:16px;width:90px;height:100px;border-radius:14px;background:linear-gradient(180deg,#1c1c1c,#3d3d3d 50%,#b7d97a)}
.bundle .label{position:absolute;left:0;right:0;top:126px;text-align:center;color:var(--white);font-style:italic;font-weight:800;font-size:24px}

/* footer */
.hygiene{position:absolute;left:130px;top:994px;color:var(--white);font-style:italic;font-weight:600;font-size:25px}
.sparkle{position:absolute;left:84px;top:984px}
.footer-rule{position:absolute;left:175px;width:560px;height:2px;background:linear-gradient(90deg,transparent,var(--white) 20%,var(--white) 80%,transparent)}
.cta{position:absolute;left:0;width:909px;top:1066px;text-align:center;color:var(--white);font-style:italic;font-weight:900;font-size:54px;line-height:1}
.cta em{color:var(--green);font-style:italic}
.audience{position:absolute;left:0;width:909px;top:1134px;text-align:center;color:var(--white);font-weight:500;font-style:italic;font-size:22px;letter-spacing:6px}
</style>
</head>
<body>
<div class="flyer">

  <header class="header">
    <div class="title-rule" style="top:44px"></div>
    <h1 class="title">RENNSTRECKEN-COACHING</h1>
    <div class="title-rule" style="top:122px"></div>
    <p class="price-line">NUR <span class="amount">349€</span> PRO FAHRER</p>
  </header>

  <div class="middle"></div>
  <div class="track-photo" role="img" aria-label="Foto einer Rennstrecke mit rot-weißem Curb"></div>
  <div class="rider-photo" role="img" aria-label="Foto eines Motorradfahrers in Schräglage auf grün-schwarzer Rennmaschine"></div>

  <div class="tab" style="top:336px;width:409px;height:47px">IM PREIS ENTHALTEN:</div>

  <section class="included">
    <div class="item" style="left:0;width:252px">
      <div class="photo" role="img" aria-label="Foto eines grün-schwarzen Supersport-Motorrads" style="width:150px;background:linear-gradient(160deg,#1c1c1c,#3c3c3c 40%,var(--green-bright) 60%,#1c1c1c)"></div>
      <p class="label">Veltrona R-400</p>
    </div>
    <div class="item" style="left:252px;width:96px">
      <div class="photo" role="img" aria-label="Foto eines Benzinkanisters" style="width:46px;background:linear-gradient(180deg,#2a2a2a,#111)"></div>
      <p class="label">Sprit</p>
    </div>
    <div class="item" style="left:348px;width:186px">
      <div class="photo" role="img" aria-label="Foto von Reifenwärmern" style="width:110px;background:linear-gradient(90deg,#1a1a1a,#3a3a3a 30%,var(--green-bright) 50%,#3a3a3a 70%,#1a1a1a)"></div>
      <p class="label">Reifenwärmer</p>
    </div>
    <div class="item" style="left:534px;width:283px">
      <div class="photo" role="img" aria-label="Foto von zwei schwarzen Motorradhelmen" style="left:42%;width:120px;background:linear-gradient(180deg,#3a3a3a,#0e0e0e)"></div>
      <p class="label" style="right:60px;font-size:25px">Profi-Trainer</p>
    </div>
  </section>

  <div class="tab" style="top:579px;width:439px;height:43px">TRAININGS PROGRAMM</div>

  <section class="programme">
    <ul>
      <li><svg width="22" height="18" viewBox="0 0 22 18"><path d="M2 9l6 6L20 2" fill="none" stroke="#76a53c" stroke-width="4"/></svg>MINDESTENS 6 TURNS À 20 MINUTEN</li>
      <li><svg width="22" height="18" viewBox="0 0 22 18"><path d="M2 9l6 6L20 2" fill="none" stroke="#76a53c" stroke-width="4"/></svg>3,5 STUNDEN INTENSIVTRAINING</li>
    </ul>
  </section>

  <div class="tab" style="top:748px;width:592px;height:46px">OPTIONALE SCHUTZAUSRÜSTUNG:</div>

  <section class="equipment">
    <div class="item" style="left:0;width:206px">
      <div class="photo" role="img" aria-label="Foto einer schwarz-weißen Lederkombi" style="left:62%;background:linear-gradient(180deg,#1a1a1a,#4a4a4a 50%,#cfcfcf)"></div>
      <span class="badge">59€</span>
      <p class="label">Lederkombi</p>
    </div>
    <div class="item" style="left:206px;width:145px">
      <div class="photo" role="img" aria-label="Foto eines schwarz-grünen Motorradhelms" style="left:62%;width:78px;background:linear-gradient(160deg,#1a1a1a,#3a3a3a 55%,var(--green-bright))"></div>
      <span class="badge" style="left:8px">29€</span>
      <p class="label">Helm</p>
    </div>
    <div class="item" style="left:351px;width:158px">
      <div class="photo" role="img" aria-label="Foto von weiß-schwarzen Motorradstiefeln" style="left:58%;width:80px;background:linear-gradient(180deg,#e8e8e8,#9a9a9a 60%,#1a1a1a)"></div>
      <span class="badge" style="left:10px">29€</span>
      <p class="label small">Stiefel</p>
    </div>
    <div class="item" style="left:509px;width:167px">
      <div class="photo" role="img" aria-label="Foto von grün-schwarzen Motorradhandschuhen" style="top:56px;width:130px;height:52px;background:linear-gradient(90deg,#1a1a1a,var(--green-bright) 40%,#1a1a1a 70%,var(--green-bright))"></div>
      <span class="badge" style="left:22px">19€</span>
      <p class="label small">Handschuhe</p>
    </div>
  </section>

  <section class="bundle">
    <span class="amount">99€</span>
    <div class="photo" role="img" aria-label="Foto einer schwarz-grünen Schutzweste"></div>
    <p class="label">KOMPLETTPAKET</p>
  </section>

  <svg class="sparkle" width="44" height="44" viewBox="0 0 44 44" aria-hidden="true">
    <path d="M16 2 L19 13 L30 16 L19 19 L16 30 L13 19 L2 16 L13 13 Z" fill="#8cc63f"/>
    <path d="M33 26 L35 32 L41 34 L35 36 L33 42 L31 36 L25 34 L31 32 Z" fill="#8cc63f"/>
  </svg>
  <p class="hygiene">Sämtliche Leih-Ausrüstung wird stets mit Ozondesinfiziert und gereinigt.</p>

  <div class="footer-rule" style="top:1052px"></div>
  <p class="cta">JETZT <em>BUCHEN</em> &amp; <em>DURCHSTARTEN!</em></p>
  <div class="footer-rule" style="top:1122px;background:linear-gradient(90deg,transparent,var(--green) 20%,var(--green) 80%,transparent)"></div>
  <p class="audience">FÜR EINSTEIGER &amp; FORTGESCHRITTENE</p>

</div>
</body>
</html>
```